Business cards for our company

We are a new online eLearning company. We create training for organizations that need to comply with governmental regulations. Our courses are built around the concept of an online show so our course has a media player / control bar across the bottom of all courses. We think this is an important element to work into the design. We have a simple mock up which we don't want anyone to just follow but just to give some idea of how the control bar could be used in the design but we are open to anything creative. If you choose to use the control bar, it doesn't have to be used literally. You can add/move/change buttons to suite your design concept. I have most of these files as PSD files so if you, need those just ask and I will post. The font in the course is Open Sans.
Also attached are the logo design and specs.

Target Market(s)

US corporations. Buyers are Senior HR executives, Chief Compiance Officer and General Counsels

Industry/Entity Type

Business

Contact Information for Business Card

Standard size cards. If it helps make the design more impactful, we'll do raised lettering

Font styles to use
Other font styles liked:
• Open Sans

Requirements
Must have
• must use our icon and logo using the supplied standards. needs to include our tag line as shown on the Word document (open to suggestions there as well). Should visually communicate that we are a next-generation eLearning company and not creating the same-old powerpoint looking, click next, click next type of training.

```html
<!DOCTYPE html>
<html lang="en">
<head>
<meta charset="utf-8">
<title>Veralume Business Card</title>
<link href="https://fonts.googleapis.com/css2?family=Open+Sans:wght@400;600;700&display=swap" rel="stylesheet">
<style>
  :root {
    --backdrop: #2b2b2b;
    --card-light: #ffffff;
    --card-shade: #e4e4e4;
    --brand-blue: #1b8fc4;
    --brand-blue-deep: #137aa9;
    --logo-blue: #1a6fa8;
    --player-black: #111111;
    --player-bar: #2a2a2a;
    --ink-dark: #111820;
    --ink-soft: #e6f2f9;
    --track: #555555;
  }
  html, body {
    margin: 0;
    padding: 0;
    width: 1200px;
    height: 997px;
    overflow: hidden;
    background: var(--backdrop);
  }
  .stage {
    position: relative;
    width: 1200px;
    height: 997px;
  }
  .business-card {
    position: absolute;
    left: 150px;
    top: 241px;
    width: 900px;
    height: 514px;
    font-family: "Open Sans", Arial, sans-serif;
  }
  .business-card svg { display: block; }
  .brand-name { font-weight: 600; font-size: 58px; fill: var(--logo-blue); letter-spacing: 2px; }
  .brand-tagline { font-weight: 700; font-size: 17px; fill: var(--brand-blue); letter-spacing: 0.5px; }
  .player-time { font-size: 9px; fill: #cfcfcf; }
  .person-name { font-weight: 400; font-size: 27px; fill: var(--ink-dark); }
  .person-title { font-weight: 400; font-size: 19px; fill: var(--ink-soft); }
  .web-address { font-weight: 700; font-size: 21px; fill: #ffffff; }
  .contact-line { font-weight: 400; font-size: 18px; fill: var(--ink-dark); }
  .contact-icon { fill: #e9f4fa; }
</style>
</head>
<body>
<main class="stage">
  <section class="business-card" aria-label="Veralume business card">
    <svg width="900" height="514" viewBox="0 0 900 514" xmlns="http://www.w3.org/2000/svg">
      <defs>
        <linearGradient id="cardStock" x1="0" y1="0" x2="1" y2="1">
          <stop offset="0" stop-color="var(--card-light)"/>
          <stop offset="1" stop-color="var(--card-shade)"/>
        </linearGradient>
        <linearGradient id="screenGlow" x1="0" y1="0" x2="0" y2="1">
          <stop offset="0" stop-color="#ffffff"/>
          <stop offset="1" stop-color="#e2e2e2"/>
        </linearGradient>
        <clipPath id="cardShape">
          <rect x="0" y="0" width="900" height="514" rx="30"/>
        </clipPath>
      </defs>

      <g clip-path="url(#cardShape)">
        <rect class="card-face" x="0" y="0" width="900" height="514" fill="url(#cardStock)"/>
        <polygon class="accent-band" points="125,330 705,330 900,215 900,514 30,514" fill="var(--brand-blue)"/>
      </g>

      <!-- media player frame -->
      <g class="media-player">
        <rect class="player-frame" x="125" y="28" width="580" height="312" rx="14" fill="var(--player-black)"/>
        <rect class="player-screen" x="140" y="42" width="550" height="252" rx="10" fill="url(#screenGlow)"/>
        <rect class="control-bar" x="140" y="300" width="550" height="30" rx="4" fill="var(--player-bar)"/>
        <polygon class="play-button" points="152,309 152,321 161,315" fill="#d8d8d8"/>
        <rect class="progress-track" x="172" y="313" width="430" height="4" rx="2" fill="var(--track)"/>
        <rect class="progress-fill" x="172" y="313" width="190" height="4" rx="2" fill="var(--brand-blue)"/>
        <circle class="progress-knob" cx="362" cy="315" r="4" fill="#ffffff"/>
        <text class="player-time" x="612" y="318">0:34</text>
        <g class="volume-icon" fill="#d8d8d8">
          <rect x="640" y="311" width="4" height="8"/>
          <polygon points="644,311 650,306 650,324 644,319"/>
        </g>
        <g class="fullscreen-icon" stroke="#d8d8d8" stroke-width="2" fill="none">
          <path d="M664 313 v-5 h5 M679 308 h5 v5 M684 317 v5 h-5 M669 322 h-5 v-5"/>
        </g>

        <!-- brand lockup on screen -->
        <rect class="brand-square" x="180" y="120" width="80" height="80" rx="16" fill="var(--brand-blue)"/>
        <text class="brand-name" x="282" y="172">VERALUME</text>
        <text class="brand-tagline" x="288" y="198">online eLearning company</text>
      </g>

      <!-- contact details -->
      <g class="contact-details">
        <text class="contact-line" x="838" y="290" text-anchor="end">646-555-0148</text>
        <g class="contact-icon phone-icon">
          <path d="M848 278 q8 -6 16 0 l-2 4 h-3 v-2 h-6 v2 h-3 z"/>
          <rect x="851" y="284" width="10" height="7" rx="1"/>
        </g>
        <text class="contact-line" x="838" y="322" text-anchor="end">646-555-0149</text>
        <g class="contact-icon fax-icon">
          <rect x="852" y="308" width="8" height="5"/>
          <rect x="848" y="313" width="16" height="8" rx="1"/>
          <rect x="851" y="320" width="10" height="4" fill="#9fd0e8"/>
        </g>
        <text class="contact-line" x="838" y="360" text-anchor="end">dana.whitcombe@veralume.com</text>
        <g class="contact-icon mail-icon">
          <rect x="848" y="348" width="16" height="11" rx="1"/>
          <path d="M848 348 l8 6 l8 -6" stroke="var(--brand-blue-deep)" stroke-width="1.2" fill="none"/>
        </g>
      </g>

      <!-- person -->
      <g class="person-block">
        <text class="person-name" x="80" y="420">DANA WHITCOMBE</text>
        <text class="person-title" x="80" y="448">CEO</text>
        <text class="web-address" x="80" y="478">www.Veralume.com</text>
      </g>
    </svg>
  </section>
</main>
</body>
</html>
```